Energy trading company (Voltrisa) needs a business card

We need a business card for a company based in Central America. Our main purpose is trading energy . We already have the logo but we need some good creativity to design a high impact business card. Colors blue, orange, green can be used or we would like to see good combinatios with our logo

Target Market(s)

Energy

Industry/Entity Type

Power Generation

Contact Information for Business Card

Logo , headquarters , name, background

Font styles to use
Serif
Sans Serif

Colors

Designer to choose colors to be used in the design.

Requirements
Must have
• it must have a fresh and clean view
Nice to have
• good backgrounds that combine with the logo
Should not have
• too much words

```html
<!DOCTYPE html>
<html lang="en">
<head>
<meta charset="utf-8">
<title>Voltrisa Business Card</title>
<link href="https://fonts.googleapis.com/css2?family=Lato:wght@400;700&family=Arimo:wght@700&display=swap" rel="stylesheet">
<style>
  :root {
    --backdrop: #646464;
    --card-light: #ffffff;
    --card-dark: #252324;
    --brand-orange: #f7941d;
    --ink: #1c1c1c;
    --text-white: #ffffff;
  }
  * { margin: 0; padding: 0; box-sizing: border-box; }
  html, body { width: 1200px; height: 900px; overflow: hidden; }
  body {
    background: var(--backdrop);
    position: relative;
    font-family: "Lato", Arial, sans-serif;
  }
  .card {
    position: absolute;
    top: 200px;
    width: 310px;
    height: 502px;
  }
  .card--front {
    left: 253px;
    background: var(--card-light);
    border-radius: 62px 0 62px 0;
  }
  .card--back {
    left: 627px;
    background: var(--card-dark);
    border-radius: 0 62px 0 62px;
  }
  .brand-mark {
    position: absolute;
    left: 124px;
    top: 92px;
    width: 62px;
    height: 62px;
    border-radius: 50%;
    background: var(--brand-orange);
  }
  .brand-name {
    position: absolute;
    left: 0;
    width: 100%;
    top: 156px;
    text-align: center;
    font-size: 44px;
    font-weight: 400;
    letter-spacing: 0.5px;
    color: var(--ink);
  }
  .contact {
    position: absolute;
    left: 33px;
    top: 328px;
    color: var(--ink);
  }
  .contact__name {
    font-family: "Arimo", Arial, sans-serif;
    font-weight: 700;
    font-size: 18px;
    color: var(--brand-orange);
    line-height: 20px;
  }
  .contact__role {
    font-size: 14px;
    line-height: 17px;
    margin-bottom: 6px;
  }
  .contact__line {
    display: flex;
    align-items: center;
    gap: 4px;
    font-size: 14px;
    line-height: 19px;
  }
  .contact__icon { width: 13px; height: 13px; flex: none; }
  .contact__address {
    margin-top: 7px;
    font-size: 14px;
    line-height: 18px;
  }
  .back-name {
    position: absolute;
    left: 0;
    width: 100%;
    top: 222px;
    text-align: center;
    font-size: 44px;
    font-weight: 700;
    color: var(--brand-orange);
  }
  .back-web {
    position: absolute;
    left: 0;
    width: 100%;
    top: 443px;
    text-align: center;
    font-size: 14px;
    color: var(--text-white);
  }
</style>
</head>
<body>
  <section class="card card--front">
    <div class="brand-mark" aria-hidden="true"></div>
    <div class="brand-name">VOLTRISA</div>
    <div class="contact">
      <div class="contact__name">DANIEL REYES</div>
      <div class="contact__role">Managing Director</div>
      <div class="contact__line">
        <svg class="contact__icon" viewBox="0 0 13 13" aria-hidden="true">
          <path d="M1 5 Q6.5 1 12 5 L10.5 6.5 L8.5 5.5 L8.5 4.5 Q6.5 3.8 4.5 4.5 L4.5 5.5 L2.5 6.5 Z" fill="var(--brand-orange)"/>
          <rect x="3" y="7" width="7" height="5" rx="1" fill="var(--brand-orange)"/>
        </svg>
        <span>044-987 654 321</span>
      </div>
      <div class="contact__line">
        <svg class="contact__icon" viewBox="0 0 13 13" aria-hidden="true">
          <rect x="0.5" y="2.5" width="12" height="8" fill="var(--brand-orange)"/>
          <path d="M0.5 2.5 L6.5 7 L12.5 2.5" fill="none" stroke="#fff" stroke-width="1"/>
        </svg>
        <span>hello@voltrisa.com</span>
      </div>
      <div class="contact__line">
        <svg class="contact__icon" viewBox="0 0 13 13" aria-hidden="true">
          <circle cx="6.5" cy="6.5" r="6" fill="var(--brand-orange)"/>
          <path d="M3 4 Q5 3 6 5 Q5 7 7 8 L6 11" fill="none" stroke="#fff" stroke-width="1"/>
        </svg>
        <span>www.voltrisa.com</span>
      </div>
      <div class="contact__address">88, Harbor Street<br>San Marcos, 10482</div>
    </div>
  </section>

  <section class="card card--back">
    <div class="back-name">VOLTRISA</div>
    <div class="back-web">www.voltrisa.com</div>
  </section>
</body>
</html>
```